Baby prediction and advice cards, thank you notes, Baby shower invitations and diaper raffle tickets

Please see attached brief with description of the project.

*** Only apply if you are DETAIL ORIENTED and willing to read 100% the brief and the correction instructions (if required)***

*** Only apply if you are able to communicate in English 100%***

We need QUALITY over quantity

Contact us if you have questions.

Thank you

Target Market(s)

Expecting mothers and their families (Mothers, sisters)

Font styles to use
Sans Serif

Colors

Designer to choose colors to be used in the design.

Requirements
Must have
• Read the brief
Should not have
• Read the brief

```html
<!DOCTYPE html>
<html lang="en">
<head>
<meta charset="utf-8">
<title>Baby Shower Invitation and Diaper Raffle Ticket</title>
<link rel="stylesheet" href="https://fonts.googleapis.com/css2?family=Noto+Sans:ital,wght@0,400;0,700;1,700&family=Noto+Serif:wght@700&display=swap">
<style>
  :root {
    --backdrop: #efe9df;
    --kraft: #b98f61;
    --kraft-light: #c59c6c;
    --ink: #3b2612;
    --ink-soft: #5a3d22;
    --ornament-a: #6b4a2b;
    --ornament-b: #a57c50;
  }
  * { box-sizing: border-box; margin: 0; padding: 0; }
  html, body { width: 1200px; height: 800px; overflow: hidden; }
  body {
    background: var(--backdrop);
    position: relative;
    font-family: "Noto Sans", sans-serif;
    color: var(--ink);
  }
  .card {
    position: absolute;
    background: radial-gradient(circle at 40% 40%, var(--kraft-light), var(--kraft));
  }
  .ornament-band {
    position: absolute;
    left: 0; top: 0; width: 100%;
    background: linear-gradient(180deg, var(--ornament-a) 0%, var(--ornament-b) 55%, rgba(185,143,97,0) 100%);
    opacity: 0.55;
  }
  .abs { position: absolute; }
  .center { left: 0; width: 100%; text-align: center; }

  /* Invitation */
  .invitation { left: 150px; top: 90px; width: 440px; height: 620px; }
  .invitation .ornament-band { height: 110px; }
  .invitation .lead { font-size: 16px; color: var(--ink-soft); }
  .invitation .headline {
    font-weight: 700; font-style: italic;
    font-size: 33px; line-height: 37px; color: var(--ink);
  }
  .invitation .honoring {
    font-weight: 700; font-style: italic; font-size: 20px; color: var(--ink);
  }
  .detail-row { position: absolute; left: 0; width: 100%; height: 26px; }
  .detail-label {
    position: absolute; right: 268px; top: 0;
    font-size: 20px; color: var(--ink-soft); white-space: nowrap;
  }
  .detail-line {
    position: absolute; left: 181px; width: 177px; bottom: 0;
    border-bottom: 2px solid var(--ink);
  }

  /* Diaper raffle ticket */
  .raffle { left: 680px; top: 482px; width: 400px; height: 228px; }
  .raffle .ornament-band { height: 78px; }
  .raffle .title {
    font-weight: 700; font-style: italic; font-size: 27px; line-height: 30px; color: var(--ink);
  }
  .raffle .note {
    font-weight: 700; font-style: italic; font-size: 9px; line-height: 12px; color: var(--ink);
  }
  .raffle .name-label {
    left: 107px; top: 198px;
    font-family: "Noto Serif", serif; font-weight: 700; font-size: 14px; color: var(--ink);
  }
  .raffle .name-line {
    left: 162px; top: 213px; width: 130px; border-bottom: 1.5px solid var(--ink);
  }
</style>
</head>
<body>

<section class="card invitation" aria-label="Baby shower invitation">
  <div class="ornament-band" role="img" aria-label="Swirling floral and dandelion ornament with small butterflies"></div>
  <p class="abs center lead" style="top:113px;">Celebratin</p>
  <p class="abs center lead" style="top:143px;">a</p>
  <h1 class="abs center headline" style="top:168px;">Baby on<br>the way</h1>
  <p class="abs center honoring" style="top:265px;">Join us for a shower honoring:</p>

  <div class="detail-row" style="top:317px;"><span class="detail-label">Date:</span><span class="detail-line"></span></div>
  <div class="detail-row" style="top:357px;"><span class="detail-label">Time:</span><span class="detail-line"></span></div>
  <div class="detail-row" style="top:398px;"><span class="detail-label">Place:</span><span class="detail-line"></span></div>
  <div class="detail-row" style="top:438px;"><span class="detail-label">Details:</span><span class="detail-line"></span></div>
  <div class="detail-row" style="top:478px;"><span class="detail-label">RSVP to:</span><span class="detail-line"></span></div>
  <div class="detail-row" style="top:519px;"><span class="detail-label">Hosted by:</span><span class="detail-line"></span></div>
</section>

<section class="card raffle" aria-label="Diaper raffle ticket">
  <div class="ornament-band" role="img" aria-label="Swirling floral and dandelion ornament with small butterflies"></div>
  <h2 class="abs center title" style="top:84px;">Diaper raffle<br>ticket</h2>
  <p class="abs center note" style="top:155px;">Bring a pack of diapers (any size)<br>for your chance to win a prize!</p>
  <span class="abs name-label">NAME:</span>
  <span class="abs name-line"></span>
</section>

</body>
</html>
```